Australian Civil Construction, Quarry & Mining Services needs a business card

We need a business card designed for our Civil Construction, Quarry & Mining Services based in the country in Australia.
Our Company Brindle Earthworks provide innovate solutions for infrastructure, agricultural and mining (aggregate, sand, roadbase) industry.
We would like our business cards to be double sided
Front of card: black background or something that resembles our business colours. (it doesn't have to be black we are open to options)
- Company name - Brindle Earthworks
- Either our logo or some sort of icon/picture that resembles our business
- Website - https://brindleearthworks-example.com.au/
- We will have a number of different names, positions descriptions, phone numbers and emails on separate cards for each of our managers/directors

```html
<!DOCTYPE html>
<html lang="en">
<head>
<meta charset="utf-8">
<title>Brindle Earthworks – Business Card</title>
<link href="https://fonts.googleapis.com/css2?family=Montserrat:wght@400;500;600;700&display=swap" rel="stylesheet">
<style>
  :root {
    --backdrop: #d9dcdf;
    --card-black: #151112;
    --card-white: #ffffff;
    --accent-orange: #f7841f;
    --ink: #1a1a1a;
    --muted: #555555;
    --watermark: #f2f2f2;
  }
  * { margin: 0; padding: 0; box-sizing: border-box; }
  html, body {
    width: 1200px; height: 900px; overflow: hidden;
    background: var(--backdrop);
    font-family: 'Montserrat', sans-serif;
  }
  .stage {
    width: 1200px; height: 900px;
    display: flex; flex-direction: column; align-items: center; justify-content: center;
    gap: 60px;
  }
  .card {
    position: relative;
    width: 600px; height: 340px;
    border-radius: 20px;
    overflow: hidden;
    box-shadow: 0 10px 28px rgba(0,0,0,0.18);
  }

  /* Front */
  .card-front {
    background: var(--card-black);
    color: #fff;
    display: flex; flex-direction: column; align-items: center;
    padding-top: 46px;
  }
  .brand-disc {
    width: 150px; height: 150px; border-radius: 50%;
    background: var(--card-white);
  }
  .brand-name {
    margin-top: 26px;
    font-size: 22px; font-weight: 700; letter-spacing: 1px;
    text-transform: uppercase;
  }
  .brand-tagline {
    margin-top: 34px;
    font-size: 12.5px; font-weight: 500; letter-spacing: 1px;
    text-transform: uppercase;
  }

  /* Back */
  .card-back { background: var(--card-white); }
  .watermark-disc {
    position: absolute; left: 190px; top: 20px;
    width: 250px; height: 250px; border-radius: 50%;
    background: var(--watermark);
  }
  .holder {
    position: absolute; left: 52px; top: 128px;
  }
  .holder-name {
    font-size: 30px; font-weight: 700; color: var(--ink); white-space: nowrap;
  }
  .holder-name .surname { color: var(--accent-orange); }
  .holder-role {
    margin-top: 2px; margin-left: 112px;
    font-size: 14px; font-weight: 400; color: var(--muted);
  }
  .divider {
    position: absolute; left: 318px; top: 72px;
    width: 1.5px; height: 112px; background: var(--accent-orange);
  }
  .contact {
    position: absolute; left: 334px; top: 62px;
    font-size: 13px; color: var(--muted); line-height: 1.4;
  }
  .contact-address { margin-bottom: 10px; }
  .contact-row { display: flex; align-items: center; gap: 7px; }
  .contact-row svg { width: 11px; height: 11px; flex: none; }
  .card-base { position: absolute; left: 0; bottom: 0; width: 600px; height: 340px; }
</style>
</head>
<body>
<main class="stage">
  <section class="card card-front" aria-label="Business card front">
    <div class="brand-disc"></div>
    <h1 class="brand-name">Brindle Earthworks</h1>
    <p class="brand-tagline">Civil Construction, Quarry &amp; Mining Services</p>
  </section>

  <section class="card card-back" aria-label="Business card back">
    <div class="watermark-disc"></div>
    <div class="holder">
      <h2 class="holder-name">Marla <span class="surname">Quintero</span></h2>
      <p class="holder-role">Payroll Manager</p>
    </div>
    <div class="divider"></div>
    <div class="contact">
      <p class="contact-address">418 Ridgeline Rd.<br>Suite 12 Toowoomba QLD 4350</p>
      <p class="contact-row">
        <svg viewBox="0 0 12 12"><path d="M2.5 1 L4.5 1 L5.2 3.6 L4 4.6 Q5 7 7.4 8 L8.4 6.8 L11 7.5 L11 9.5 Q11 11 9.5 11 Q1 10 1 2.5 Q1 1 2.5 1Z" fill="var(--accent-orange)"/></svg>
        (07) 4613 2275
      </p>
      <p class="contact-row">
        <svg viewBox="0 0 12 12"><rect x="1" y="2.5" width="10" height="7" fill="none" stroke="var(--accent-orange)" stroke-width="1.2"/><path d="M1 2.5 L6 6.5 L11 2.5" fill="none" stroke="var(--accent-orange)" stroke-width="1.2"/></svg>
        info@brindleearthworks-example.com.au
      </p>
      <p class="contact-row">
        <svg viewBox="0 0 12 12"><circle cx="6" cy="6" r="5" fill="none" stroke="var(--accent-orange)" stroke-width="1.2"/><ellipse cx="6" cy="6" rx="2.2" ry="5" fill="none" stroke="var(--accent-orange)" stroke-width="1"/><path d="M1 6 H11" stroke="var(--accent-orange)" stroke-width="1"/></svg>
        www.brindleearthworks-example.com.au
      </p>
    </div>
    <svg class="card-base" viewBox="0 0 600 340" aria-hidden="true">
      <polygon points="0,328 445,298 432,340 0,340" fill="var(--accent-orange)"/>
      <polygon points="447,290 600,290 600,340 430,340" fill="var(--card-black)"/>
    </svg>
  </section>
</main>
</body>
</html>
```